依頼詳細
■サブタイトル
*添付のPDFの見本(以下PDF)は英語ですが日本語(カタカナ)に変えてもOK
*適当な文章に変えてもOK
*サブタイトルは無くてもOK

■タイトル
*PDFは「Lumo7,inc.」ですが「ルモセブン」でもOK
*PDFの書体でなく変えてもOK
*位置は左側でなく、現在のHPのように左右センターでもOK

■タイトル右側の空白部分
*可能ならイメージカットを入れるかデザイン処理を希望
*ごちゃごちゃするようなら、空白のままでOK

■上ナビ
*入れる文字はPDF同様の項目を使用
(必要に応じてデザイン処理を希望)

■トップページ本文
*PDFは横に4つのレイアウトですが変えてもOK
*イメージ画像はできるだけ指定通りの大きさで
(スマホ時に縦の長さを短くしたいため)
*イメージ画像は写真でもイラストでもOK
(使用例は添付ファイル参照)
*各ブロックの「詳しくはこちらをご覧ください。」は画像処理でもOK
(文章を変えてもOK)

■サブページ本文
*一部に画像を使用するか、小見出しのデザイン処理を希望

■フッター
*PDFはフッターの天地が狭く、ページ全体が横長で収まりが悪いので天地は多少広めが希望
*バランス的に問題なければ自社メディアの紹介も希望
(バナーでなくテキスト一覧が希望。サイト名は添付ファイル参照)
サイトURL
http://www.lumo7.co.jp/
ページ数
2ページ
希望イメージ
シンプル 複雑
単色 カラフル
暗い 明るい
日常 高級
遊び心 厳粛
未来的 伝統的
女性的 男性的
希望する色
色はお任せします。(基本は落ち着いた感じの色合いでお願いします)
納品ファイル
• フォトショップ形式 (.psd)
• PNG形式 (.png)
補足説明
※納品ファイルはフォトショップ形式がなければPNG形式のみでもかまいません。

★締切日当日のご提案は、採用候補でも修正依頼が出せないため、気に入った案でも候補に入れられないので、できるだけ初回のご提案は締切日の2~3日前までにいただけましたら幸いです。
メインに大きい写真を使用していただくご提案の場合は、4つのイメージ画像も写真にすると色が多すぎてしまう感じがするので、4つのイメージ画像は(多色でない)イラストにするとか、カラー写真を使用しないなどを希望します。

また、主なWEBメディア一覧を入れていただくご提案の場合は、トップページのフッターのみに入れて、サブページは不要とさせてください。
こちらを入れる目的はトップページから各サイトに被リンクを与えることですので、全ページに掲載すると逆に被リンクが多すぎてSEO的に問題があるためです。
したがって、各サイトへの誘導が目的ではありませんのでこの部分は特に目立たせる必要はなく、フッターに入れていただく場合は、さり気なくバランスよく入る場合のみでかまいません。

いろいろと希望が多くて申し訳ございませんが、よろしくお願いいたします。

全体のバランスがよくや色使いも落ち着いていて好みだったので、決めさせていただきました。
また、修正依頼などもすぐに対応いただき、助かりました。

多くのご提案をいただき、ありがとうございました。
結局は主観的な好みで決めさせていただきましたが、かなり迷ったご提案も数点ありました。
なお、締切日ギリギリのご提案は、修正依頼が出せないので、良いご提案も見送らせていただいたものもありました。

```html
<!DOCTYPE html>
<html lang="ja">
<head>
<meta charset="utf-8">
<title>Lumo7,inc.</title>
<link href="https://fonts.googleapis.com/css2?family=Noto+Sans+JP:wght@400;500;700&family=Roboto:wght@300;400&display=swap" rel="stylesheet">
<style>
:root{
  --ink:#3a3a3a;
  --muted:#777;
  --accent:#27a6c8;
  --accent-soft:#bfe6f1;
  --page-bg:#eeeeee;
  --card-bg:#ffffff;
  --button:#6d6d6d;
  --line:#d6d6d6;
  --hero-dark:#3b4046;
  --hero-light:#8a9096;
}
*{box-sizing:border-box;margin:0;padding:0}
html,body{width:852px;height:1200px;overflow:hidden}
body{font-family:"Noto Sans JP",sans-serif;color:var(--ink);background:#fff;position:relative}

.site-header{height:62px;display:flex;align-items:center;justify-content:space-between;padding:0 24px 0 22px;background:#fff}
.brand{font-family:"Roboto",sans-serif;font-weight:400;font-size:24px;letter-spacing:.5px;color:var(--ink)}
.global-nav{display:flex;gap:30px;font-size:10px;font-weight:500;margin-top:-18px}
.global-nav a{color:var(--ink);text-decoration:none;position:relative;padding-left:10px}
.global-nav a::before{content:"";position:absolute;left:0;top:5px;width:4px;height:4px;background:var(--accent)}

.hero{height:223px;position:relative;display:flex;align-items:center;justify-content:center}
.hero-image{position:absolute;inset:0;background:linear-gradient(100deg,var(--hero-dark) 0%,#596068 45%,var(--hero-light) 100%)}
.hero-title{position:relative;color:#fff;font-family:"Roboto",sans-serif;font-weight:300;font-size:19px;letter-spacing:1.5px;display:flex;align-items:center;gap:16px}
.hero-title::before,.hero-title::after{content:"";width:110px;height:1px;background:rgba(255,255,255,.6)}

.services{background:var(--page-bg);height:750px;padding-top:22px}
.service-grid{width:613px;margin:0 auto;display:grid;grid-template-columns:300px 300px;gap:13px}
.service-card{background:var(--card-bg);height:333px;position:relative;text-align:center;padding-top:22px}
.service-icon{width:110px;height:80px;margin:0 auto;border-radius:6px;background:linear-gradient(180deg,var(--accent-soft),#e4f4f9)}
.service-title{color:var(--accent);font-size:17px;font-weight:700;margin-top:22px;letter-spacing:1px}
.service-text{font-size:10px;line-height:1.85;color:var(--muted);text-align:left;padding:12px 36px 0}
.service-more{position:absolute;left:36px;right:36px;bottom:26px;height:30px;background:var(--button);color:#fff;font-size:10px;display:flex;align-items:center;justify-content:center;gap:6px;text-decoration:none}
.page-top{display:block;margin:18px auto 0;width:28px}

.site-footer{padding:14px 52px 0}
.footer-bar{display:flex;justify-content:space-between;align-items:center;font-size:9px;padding-bottom:12px;border-bottom:1px solid var(--line)}
.footer-links{display:flex;gap:26px}
.footer-links a{color:var(--ink);text-decoration:none}
.copyright{font-family:"Roboto",sans-serif;color:var(--muted);font-size:8px}
.media-list{display:flex;gap:24px;padding-top:14px;font-size:8px}
.media-heading{width:120px;font-weight:500;font-size:9px}
.media-col{list-style:none;width:170px}
.media-col li{line-height:2.1;color:var(--muted);padding-left:9px;position:relative}
.media-col li::before{content:"";position:absolute;left:0;top:7px;width:4px;height:4px;background:var(--accent)}
</style>
</head>
<body>
<header class="site-header">
  <div class="brand">Lumo7,inc.</div>
  <nav class="global-nav">
    <a href="#">WEBマーケティング</a>
    <a href="#">WEB広告</a>
    <a href="#">WEBメディア</a>
    <a href="#">ダイレクトマーケティング</a>
  </nav>
</header>

<section class="hero">
  <div class="hero-image" role="img" aria-label="ノートパソコンで作業する手元の写真"></div>
  <h1 class="hero-title">Web marketing &amp; Direct marketing Service</h1>
</section>

<main class="services">
  <div class="service-grid">
    <article class="service-card">
      <div class="service-icon" role="img" aria-label="画面とグラフのWEBマーケティングのイラスト"></div>
      <h2 class="service-title">WEBマーケティング</h2>
      <p class="service-text">ルモセブンのWEBマーケティングは、調査から分析、改善までを一貫してサポート。検索対策やサイト設計を通じて、お客様の集客と売上の向上に貢献します。</p>
      <a class="service-more" href="#">さらに詳しく <span>›</span></a>
    </article>
    <article class="service-card">
      <div class="service-icon" role="img" aria-label="ブラウザとメガホンのWEB広告のイラスト"></div>
      <h2 class="service-title">WEB広告</h2>
      <p class="service-text">検索連動型広告やディスプレイ広告など、目的に合わせた最適な広告運用をご提案します。効果測定と改善を重ね、費用対効果の高い集客を実現します。</p>
      <a class="service-more" href="#">さらに詳しく <span>›</span></a>
    </article>
    <article class="service-card">
      <div class="service-icon" role="img" aria-label="記事とスマートフォンのWEBメディアのイラスト"></div>
      <h2 class="service-title">WEBメディア</h2>
      <p class="service-text">自社で運営する複数のWEBメディアを通じて、役立つ情報を発信しています。ユーザーに寄り添ったコンテンツで、多くの方にご利用いただいています。</p>
      <a class="service-more" href="#">さらに詳しく <span>›</span></a>
    </article>
    <article class="service-card">
      <div class="service-icon" role="img" aria-label="封筒と人物シルエットのダイレクトマーケティングのイラスト"></div>
      <h2 class="service-title">ダイレクトマーケティング</h2>
      <p class="service-text">顧客一人ひとりに直接届くコミュニケーションを設計します。通信販売の立ち上げから運用まで、長年の経験を活かしてトータルに支援いたします。</p>
      <a class="service-more" href="#">さらに詳しく <span>›</span></a>
    </article>
  </div>
  <svg class="page-top" viewBox="0 0 28 16" aria-label="ページトップへ"><polyline points="2,14 14,3 26,14" fill="none" stroke="#555" stroke-width="2"/></svg>
</main>

<footer class="site-footer">
  <div class="footer-bar">
    <nav class="footer-links">
      <a href="#">会社概要</a>
      <a href="#">プライバシーポリシー</a>
      <a href="#">サイトマップ</a>
      <a href="#">お問い合わせ</a>
    </nav>
    <p class="copyright">Copyright(C) Lumo7,inc. All Rights Reserved.</p>
  </div>
  <div class="media-list">
    <p class="media-heading">主なWEBメディア一覧</p>
    <ul class="media-col">
      <li>暮らしの節約ナビ</li>
      <li>転職ガイドブック</li>
      <li>住まいの相談室</li>
    </ul>
    <ul class="media-col">
      <li>カードの比較室</li>
      <li>美容のミカタ</li>
      <li>保険えらび帖</li>
    </ul>
    <ul class="media-col">
      <li>旅行プラン手帖</li>
      <li>車の買取ノート</li>
      <li>資格と学びの森</li>
    </ul>
  </div>
</footer>
</body>
</html>
```